TALLOWBROOK FREIGHT & PLANT HIRE NEEDS A FLYER

WE NEED A FLYER FOR OUR COMPANY <br/>WE SPECIALISE IN ROAD BUILDING AND MAINTENANCE, GENERAL EARTHWORK DAM REPAIRS & DESILTING, FENCE CLEARING, FIRE BREAKS, GRAVEL SOURCE AND DELIVERY GENERAL FREIGHT STEEL HAY LICK AND MCHINERY. <br/><br/>I HAVE UPLOAD A FILE THAT I LIKE AND WOULD LIKE SOMETHING THE SAME IF POSSIBLE. AND LOGO TO GO WITH IT.

```html
<!DOCTYPE html>
<html lang="en">
<head>
<meta charset="utf-8">
<title>Tallowbrook Freight &amp; Plant Hire – Flyer</title>
<link href="https://fonts.googleapis.com/css2?family=Montserrat:wght@600;700;800&display=swap" rel="stylesheet">
<style>
  :root {
    --amber: #f9a81a;
    --amber-text: #f6a020;
    --charcoal: #333335;
    --ink: #2b2b2d;
    --paper: #ffffff;
  }
  html, body {
    margin: 0;
    padding: 0;
    width: 800px;
    height: 1200px;
    overflow: hidden;
    background: var(--paper);
  }
  .flyer {
    position: relative;
    width: 800px;
    height: 1200px;
    font-family: "Montserrat", Arial, sans-serif;
    text-transform: uppercase;
    text-align: center;
  }
  .flyer__backdrop {
    position: absolute;
    inset: 0;
  }
  .tagline {
    position: absolute;
    top: 44px;
    left: 0;
    right: 0;
    margin: 0;
    font-size: 26px;
    font-weight: 700;
    letter-spacing: -0.3px;
    color: var(--ink);
  }
  .brand {
    position: absolute;
    top: 250px;
    left: 0;
    right: 0;
    color: var(--charcoal);
    font-weight: 800;
    line-height: 1;
  }
  .brand__name { font-size: 70px; letter-spacing: 1px; display: block; }
  .brand__line { font-size: 38px; display: block; margin-top: 14px; }
  .brand__suffix { font-size: 28px; display: block; margin-top: 10px; }
  .section {
    position: absolute;
    left: 30px;
    right: 30px;
  }
  .section--services { top: 618px; }
  .section--machinery { top: 830px; }
  .section__title {
    margin: 0 0 18px;
    font-size: 27px;
    font-weight: 700;
    color: var(--amber-text);
  }
  .section__list {
    margin: 0;
    font-size: 21px;
    font-weight: 600;
    line-height: 33px;
    color: var(--paper);
  }
  .contact {
    position: absolute;
    top: 1082px;
    left: 0;
    right: 0;
    color: var(--ink);
    font-weight: 600;
  }
  .contact__names { margin: 0; font-size: 22px; }
  .contact__details {
    margin: 14px 0 0;
    display: flex;
    justify-content: center;
    align-items: center;
    gap: 26px;
    text-transform: none;
    font-size: 24px;
  }
  .contact__item { display: flex; align-items: center; gap: 6px; }
  .contact__icon { width: 24px; height: 24px; fill: var(--ink); }
</style>
</head>
<body>
<main class="flyer">
  <svg class="flyer__backdrop" viewBox="0 0 800 1200" width="800" height="1200" aria-hidden="true">
    <path fill="var(--amber)" d="M0 0 H800 V150 C560 112 280 122 0 152 Z"/>
    <path fill="var(--charcoal)" d="M0 152 C280 122 560 112 800 150 V180 C560 140 280 152 0 195 Z"/>
    <path fill="var(--charcoal)" d="M0 470 C260 505 540 455 800 440 V1060 H0 Z"/>
    <path fill="var(--amber)" d="M0 540 C260 565 540 505 800 472 V545 C560 555 300 605 0 598 Z"/>
    <rect fill="var(--amber)" x="0" y="1060" width="800" height="140"/>
  </svg>

  <p class="tagline">For all you freight and plant hire needs!</p>

  <h1 class="brand">
    <span class="brand__name">Tallowbrook</span>
    <span class="brand__line">Freight &amp; Plant Hire</span>
    <span class="brand__suffix">Pty Ltd</span>
  </h1>

  <section class="section section--services">
    <h2 class="section__title">Specialising in:</h2>
    <p class="section__list">
      Road building and maintenance • General<br>
      earthworks • Dam repairs &amp; desilting • Fence<br>
      clearing • Fire breaks • Gravel source &amp; delivery<br>
      General freight • Steel • Lick • Hay • Machinery
    </p>
  </section>

  <section class="section section--machinery">
    <h2 class="section__title">Current machinery avaiable:</h2>
    <p class="section__list">
      Grader • Loader &amp; stick rack • Rollers<br>
      Dozer • Water trucks • Side tippers • Prime<br>
      movers • Forklift • Skid steer loader • Flat<br>
      tops • Drop deck
    </p>
  </section>

  <footer class="contact">
    <p class="contact__names">Dean &amp; Marla Covell</p>
    <p class="contact__details">
      <span class="contact__item">
        <svg class="contact__icon" viewBox="0 0 24 24" aria-label="Phone"><path d="M6.6 10.8a15.2 15.2 0 0 0 6.6 6.6l2.2-2.2a1 1 0 0 1 1-.25 11.4 11.4 0 0 0 3.6.57 1 1 0 0 1 1 1V20a1 1 0 0 1-1 1A17 17 0 0 1 3 4a1 1 0 0 1 1-1h3.5a1 1 0 0 1 1 1c0 1.25.2 2.45.57 3.6a1 1 0 0 1-.25 1z"/></svg>
        : 0491570156
      </span>
      <span class="contact__item">
        <svg class="contact__icon" viewBox="0 0 24 24" aria-label="Email"><path d="M2 5h20v14H2z M3.5 6.5 12 13l8.5-6.5" fill="var(--ink)" stroke="var(--amber)" stroke-width="1.6"/></svg>
        : marlacovell@tallowbrook.net
      </span>
    </p>
  </footer>
</main>
</body>
</html>
```